Copper Lark Treks Flyer

I have an adventure travel company and I need a flyer to promote my trip to Ukraine.
I would like to have a universal flyer that I can change based on the trip.
The Title should say "Travel to Ukraine: 9 Day Eastern European Adventure"
The date should be under the title.
The background photo should be kiev2.jpg
The highlights of the trip, then price $1200 and what it includes. See the text for highlights and includes sections here:
http://www.copperlarktreks.com/#!featured-trip
The website link (www.copperlarktreks.com) should be somewhere in the bottom.
You can use other photos provided or from my website that relates to Ukraine trip.

```html
<!DOCTYPE html>
<html lang="en">
<head>
<meta charset="utf-8">
<title>Copper Lark Treks – Travel to Ukraine</title>
<link rel="stylesheet" href="https://fonts.googleapis.com/css2?family=Alfa+Slab+One&family=Open+Sans:wght@400;600;700&family=Oswald:wght@600&display=swap">
<style>
  :root {
    --bg: #2b2b2b;
    --red: #e8232a;
    --white: #ffffff;
    --grey: #a9a9a9;
  }
  * { margin: 0; padding: 0; box-sizing: border-box; }
  html, body { width: 847px; height: 1200px; overflow: hidden; background: var(--bg); }
  .flyer {
    position: relative; width: 847px; height: 1200px; overflow: hidden;
    background: var(--bg); font-family: "Open Sans", Arial, sans-serif;
  }
  .flyer__title {
    position: absolute; top: 12px; left: 0; width: 100%; text-align: center;
    font-family: "Alfa Slab One", Georgia, serif; font-weight: 400; font-size: 25px;
    color: var(--red); letter-spacing: 0.2px;
    text-shadow: -1px -1px 0 var(--white), 1px -1px 0 var(--white), -1px 1px 0 var(--white), 1px 1px 0 var(--white);
  }
  .flyer__dates {
    position: absolute; top: 58px; right: 110px;
    color: var(--red); font-size: 19px;
  }
  .gallery { position: absolute; top: 84px; left: 0; width: 847px; height: 516px; }
  .gallery__photo { position: absolute; width: 282px; height: 257px; }
  .photo--cave { left: 0; top: 0; background: linear-gradient(150deg, #4a2a18, #a7774c 45%, #5c3620); }
  .photo--lavra-river { left: 284px; top: 0; width: 280px; background: linear-gradient(180deg, #9fb9d6 0%, #7c95a8 30%, #c9a43a 55%, #6b7a45 100%); }
  .photo--coast { left: 566px; top: 0; width: 281px; background: linear-gradient(180deg, #5d6670 0%, #2d5e8a 35%, #2f6f5a 60%, #3d5a2c 100%); }
  .photo--tram { left: 0; top: 259px; background: linear-gradient(180deg, #c9c3b5 0%, #9a8e7c 50%, #b2413a 70%, #7c7468 100%); }
  .photo--lavra-hill { left: 284px; top: 259px; width: 280px; background: linear-gradient(180deg, #b8cde0 0%, #d2b04a 45%, #e3ddd0 70%, #5f7a4a 100%); }
  .photo--mountain { left: 566px; top: 259px; width: 281px; background: linear-gradient(180deg, #9fb2c4 0%, #8e9388 45%, #3f5232 80%, #8c8878 100%); }

  .section-heading {
    position: absolute; top: 600px; color: var(--red);
    font-size: 19px; font-weight: 700; letter-spacing: 0.3px;
  }
  .highlights__heading { left: 14px; }
  .includes__heading { left: 460px; }

  .highlight {
    position: absolute; left: 14px; width: 430px;
    font-size: 17.5px; line-height: 25px;
  }
  .highlight--light { color: var(--white); }
  .highlight--muted { color: var(--grey); }

  .include {
    position: absolute; left: 460px; width: 380px;
    font-size: 22.5px; line-height: 34px;
  }
  .include--light { color: var(--white); }
  .include--muted { color: var(--grey); }

  .price {
    position: absolute; left: 494px; top: 1110px;
    font-family: "Oswald", "Arial Narrow", sans-serif; font-weight: 600;
    font-size: 50px; line-height: 58px; color: var(--red);
  }
  .website {
    position: absolute; right: 14px; top: 1176px;
    color: var(--red); font-size: 15px;
  }
</style>
</head>
<body>
<main class="flyer">
  <h1 class="flyer__title">Travel to Ukraine: 9 Day Eastern European Adventure</h1>
  <p class="flyer__dates">Fri May 18 - Sun may 27</p>

  <section class="gallery">
    <div class="gallery__photo photo--cave" role="img" aria-label="Crystal formations inside a limestone cave"></div>
    <div class="gallery__photo photo--lavra-river" role="img" aria-label="Golden domes of the Kiev monastery above the river and city"></div>
    <div class="gallery__photo photo--coast" role="img" aria-label="Crimean coastline with sea and forested cliffs"></div>
    <div class="gallery__photo photo--tram" role="img" aria-label="Red tram on a tree-lined cobbled street"></div>
    <div class="gallery__photo photo--lavra-hill" role="img" aria-label="White cathedral with golden domes on a green hill"></div>
    <div class="gallery__photo photo--mountain" role="img" aria-label="Pine tree on a rocky mountain ridge"></div>
  </section>

  <h2 class="section-heading highlights__heading">HIGHLIGHTS:</h2>
  <p class="highlight highlight--muted" style="top:662px">Discover Kiev- the birthplace of<br>Eastern Slavic Civilization</p>
  <p class="highlight highlight--light" style="top:738px">Meet Crimea's fascinating Tatar<br>Minority in Bakhchysaray - former<br>capital of Crimean Tatar Khans</p>
  <p class="highlight highlight--muted" style="top:832px">Walk to Chufut-Kale - Crimea's<br>best preserved&nbsp; medieval cave town</p>
  <p class="highlight highlight--light" style="top:918px">Hike in the most spectacular areas in<br>&nbsp;Karabi and explorethe caves with a<br>&nbsp;group of professional speleologist</p>
  <p class="highlight highlight--muted" style="top:1016px">Inhale the magic Yalta's air- an invigorating<br>blend of sea and pine forest sprinkled with<br>mountain chill</p>
  <p class="highlight highlight--light" style="top:1114px">Visit Odessa- "the Pearl by the Black Sea",<br>Catacombs, Opera house, the factory of<br>sparkling wines and famous Potemkin Steps</p>

  <h2 class="section-heading includes__heading">INCLUDES:</h2>
  <p class="include include--light" style="top:662px">9 nights accommodations</p>
  <p class="include include--muted" style="top:728px">Breakfast, lunch and dinner daily</p>
  <p class="include include--light" style="top:794px">English speaking tour guides and<br>transportation at every destination.</p>
  <p class="include include--muted" style="top:892px">Tour leader from USA at all times<br>during the trip.</p>
  <p class="include include--light" style="top:990px">All Group Transfers<br>(trains, buses and vans),<br>sightseeing tours and entrance fees</p>

  <p class="price">PRICE: $1200</p>
  <p class="website">www.copperlarktreks.com</p>
</main>
</body>
</html>
```